Linen Sparrow- Hand made fashion accessories

Linen sparrow is a new business that will be selling hand made fashion accessories for women such as bags, baskets, knecklaces etc. The items are all hand made from Africa. I would like natural colors leaning more to the cardboard rustic look. I would like the card to look simple but elegant at the same time.

Industry/Entity Type

Business

Contact Information for Business Card

www.linensparrow-example.com.au
sales@linensparrow-example.com.au
Tel: 0427586302

Font styles to use
Decorative
Script

Requirements
Must have
• Earthy and rustic colours. Straw, cardboard etc. Fine black cursive print. One side of card only name
• second side website, email and tel.
Should not have
• No need to have any description of what business sells or does. No pictures of anything.

```html
<!DOCTYPE html>
<html lang="en">
<head>
<meta charset="utf-8">
<title>Linen Sparrow – Business Card</title>
<link rel="stylesheet" href="https://fonts.googleapis.com/css2?family=Open+Sans:wght@400&family=Pinyon+Script&display=swap">
<style>
  :root {
    --page-bg: #ece7df;
    --card-cardboard: #c4a273;
    --card-straw: #e8d6a8;
    --card-bark: #6e5034;
    --card-shade: #3d2b1b;
    --ink-black: #141210;
    --card-shadow: rgba(40, 28, 15, 0.25);
  }
  * { margin: 0; padding: 0; box-sizing: border-box; }
  html, body {
    width: 1200px;
    height: 844px;
    overflow: hidden;
    background: var(--page-bg);
  }
  .card-sheet {
    position: relative;
    width: 1200px;
    height: 844px;
  }
  .card {
    position: absolute;
    top: 272px;
    width: 525px;
    height: 300px;
    box-shadow: 0 10px 24px var(--card-shadow);
  }
  .card--contact { left: 50px; }
  .card--name { left: 625px; }
  .card svg { display: block; width: 100%; height: 100%; }
  .fill-cardboard { fill: var(--card-cardboard); }
  .fill-straw { fill: var(--card-straw); }
  .fill-bark { fill: var(--card-bark); }
  .fill-shade { fill: var(--card-shade); }
  .contact-text {
    font-family: "Open Sans", sans-serif;
    font-size: 15px;
    fill: var(--ink-black);
  }
  .icon-stroke {
    fill: none;
    stroke: var(--card-bark);
    stroke-width: 1.4;
  }
  .brand-name {
    font-family: "Pinyon Script", cursive;
    font-size: 40px;
    fill: var(--ink-black);
  }
</style>
</head>
<body>
<main class="card-sheet">

  <!-- Contact side -->
  <section class="card card--contact" aria-label="Contact side">
    <svg viewBox="0 0 525 300" xmlns="http://www.w3.org/2000/svg">
      <rect class="fill-cardboard" width="525" height="300"/>

      <!-- contact stripes -->
      <polygon class="fill-shade" points="95,80 120,80 120,124 137,124"/>
      <rect class="fill-straw" x="110" y="80" width="415" height="44"/>
      <polygon class="fill-shade" points="150,134 175,134 175,174 188,174"/>
      <rect class="fill-straw" x="165" y="134" width="360" height="40"/>
      <polygon class="fill-shade" points="205,184 230,184 230,224 242,224"/>
      <rect class="fill-straw" x="220" y="184" width="305" height="40"/>

      <!-- corner wedge -->
      <polygon class="fill-bark" points="0,0 0,300 320,300"/>

      <text class="contact-text" x="130" y="107">0427586302</text>
      <text class="contact-text" x="185" y="159">sales@linensparrow-example.com.au</text>
      <text class="contact-text" x="238" y="209">www.linensparrow-example.com.au</text>

      <!-- phone icon -->
      <g class="contact-icon" transform="translate(62 134)">
        <circle class="fill-straw" r="12"/>
        <path class="fill-bark" d="M-5,-6 l3,-1 l2,4 l-2,1.5 q1.5,3.5 4,5 l1.5,-2 l4,2 l-1,3 q-7,0 -11.5,-12.5z"/>
      </g>
      <!-- email icon -->
      <g class="contact-icon" transform="translate(117 186)">
        <circle class="fill-straw" r="12"/>
        <rect class="fill-bark" x="-6.5" y="-4.5" width="13" height="9" rx="1"/>
        <path d="M-6,-4 L0,1 L6,-4" fill="none" stroke="#e8d6a8" stroke-width="1.2"/>
      </g>
      <!-- web icon -->
      <g class="contact-icon" transform="translate(172 238)">
        <circle class="fill-straw" r="12"/>
        <circle class="icon-stroke" r="6.5"/>
        <ellipse class="icon-stroke" rx="2.8" ry="6.5"/>
        <line class="icon-stroke" x1="-6.5" y1="0" x2="6.5" y2="0"/>
      </g>
    </svg>
  </section>

  <!-- Name side -->
  <section class="card card--name" aria-label="Name side">
    <svg viewBox="0 0 525 300" xmlns="http://www.w3.org/2000/svg">
      <rect class="fill-cardboard" width="525" height="300"/>
      <polygon class="fill-shade" points="115,112 160,112 160,190 200,190"/>
      <rect class="fill-straw" x="150" y="112" width="375" height="78"/>
      <polygon class="fill-bark" points="0,0 0,300 255,300"/>
      <text class="brand-name" x="372" y="163" text-anchor="middle">Linen sparrow</text>
    </svg>
  </section>

</main>
</body>
</html>
```